Website for an interior designer

We need a new website for Clara Beth Holloway whose new business name is Clara Beth Holloway Interiors. She is a residential interior designer with a mix of modern and contemporary tastes. We are in the process of overhauling her website which is +15 years old and not an accurate reflection of her tastes. The uploaded photos are from some of the houses she has done as well as her logo(s). We would need a section for "About Us" that would have a paragraph of text and bullets showing services and a gallery for photos (~12 total, more to come). A contract page would be optional. The client likes the feel/look of this website: https://www.pondrickstudio.example/ but doesn't want to copy it exactly.

Target Market(s)

Upscale home owners

Industry/Entity Type

Interior Design

Coding

Coded - Design and coding required

Number of Pages Required

4 page

Colors

Designer to choose only greyscale colors for use in the design.

Requirements
Must have
• Home page, about us page, gallery page, contact us page.

```html
<!DOCTYPE html>
<html lang="en">
<head>
<meta charset="utf-8">
<title>Clara Beth Holloway Interiors</title>
<link href="https://fonts.googleapis.com/css2?family=Cinzel:wght@400;500&family=Mulish:wght@400;500&family=Poppins:wght@600;700&display=swap" rel="stylesheet">
<style>
:root{
  --band:#b3b6b5;
  --band-soft:#e6e7e7;
  --accent:#8a8a8a;
  --accent-light:#a8a8a8;
  --ink:#2f3132;
  --text:#454545;
  --muted:#8f9190;
  --white:#ffffff;
  --serif:'Cinzel', serif;
  --sans:'Mulish', sans-serif;
  --display:'Poppins', sans-serif;
}
*{margin:0;padding:0;box-sizing:border-box}
html,body{width:1200px;height:2835px;overflow:hidden;background:var(--white)}
body{position:relative;font-family:var(--sans);color:var(--text)}
.abs{position:absolute}

/* header */
.brand{left:142px;top:22px;width:220px;text-align:center;font-family:var(--serif);color:var(--ink)}
.brand-name{font-size:15px;letter-spacing:1px;line-height:1.3}
.brand-sub{font-size:8px;letter-spacing:4px;margin-top:4px;display:flex;align-items:center;justify-content:center;gap:8px}
.brand-sub::before,.brand-sub::after{content:"";width:22px;height:1px;background:var(--ink)}
.brand-dot{width:22px;height:22px;border:1px solid var(--ink);border-radius:50%;margin:0 auto 6px}
.nav{top:56px;left:538px;display:flex;font-family:var(--serif);font-size:13.5px;letter-spacing:.6px;color:var(--ink)}
.nav a{color:inherit;text-decoration:none;margin-right:44px}
.nav a.active{color:var(--accent)}
.nav a:last-child{margin-right:0}

/* buttons */
.btn{display:inline-block;background:var(--ink);color:var(--white);font-family:var(--sans);font-size:13.5px;letter-spacing:.5px;padding:0 18px;height:39px;line-height:39px;position:absolute}
.btn::after{content:"";position:absolute;left:6px;top:6px;right:-6px;bottom:-6px;border:1px solid var(--accent-light);z-index:-1}

/* hero */
.hero-circle{left:368px;top:507px;width:196px;height:196px;border-radius:50%;background:var(--band-soft)}
.hero-photo{left:436px;top:111px;width:764px;height:556px;background:linear-gradient(180deg,#e3e5e6 0%,#c8c6c3 45%,#7d7673 75%,#6e746d 100%)}
.hero-kicker{left:142px;top:281px;font-family:var(--serif);font-size:13px;letter-spacing:1px;color:var(--muted)}
.hero-title{left:139px;top:306px;font-family:var(--display);font-weight:700;font-size:35px;line-height:44px;color:var(--ink);z-index:2}
.hero-title span{color:var(--accent)}

/* split sections */
.block-band{background:var(--band)}
.section-title{font-family:var(--serif);font-size:28px;font-weight:500;color:var(--ink);letter-spacing:.5px}
.rule{width:42px;height:2px;background:var(--accent)}
.about-text{left:610px;top:995px;width:452px;font-size:14.5px;line-height:28.3px;letter-spacing:.3px}
.service-list{left:141px;top:1580px;list-style:none;font-size:14.5px;color:var(--ink)}
.service-list li{height:36.7px;line-height:24px}
.service-list li::before{content:"•";color:var(--muted);margin-right:4px}

/* gallery */
.gallery-band{left:0;top:2004px;width:1200px;height:230px;background:var(--band)}
.gallery-title{left:0;width:1200px;top:2080px;text-align:center;font-family:var(--serif);font-size:27px;color:var(--white);letter-spacing:.5px}
.gallery-rule{left:579px;top:2135px;width:42px;height:2px;background:var(--white);opacity:.8}
.tile{top:2169px;width:222px;height:255px;background:var(--white);padding:5px}
.tile div{width:100%;height:100%}
.swatch{top:2381px;width:33px;height:84px}

/* footer */
.foot-head{top:2584px;font-family:var(--serif);font-size:15px;color:var(--ink);letter-spacing:.5px}
.foot-links{left:142px;top:2610px;list-style:none;font-size:13px;color:var(--ink)}
.foot-links li{height:25.5px;line-height:20px}
.foot-links li::before{content:"»";color:var(--accent);margin-right:9px}
.contact-item{font-size:13px;color:var(--ink);display:flex;gap:8px}
.social{font-size:13px;color:var(--ink);display:flex;align-items:center;gap:10px}
.social i{width:24px;height:24px;border-radius:50%;background:var(--ink);display:inline-block}
.foot-mark{left:880px;top:2625px;width:200px;text-align:center;font-family:var(--serif);font-size:24px;line-height:34px;color:var(--ink)}
.bottom-bar{left:0;top:2796px;width:1200px;height:39px;background:var(--band);color:var(--white);font-size:11.5px;text-align:center;line-height:39px}
</style>
</head>
<body>

<header>
  <div class="abs brand">
    <div class="brand-dot"></div>
    <div class="brand-name">CLARA BETH HOLLOWAY</div>
    <div class="brand-sub">INTERIORS</div>
  </div>
  <nav class="abs nav">
    <a class="active" href="#">HOME</a>
    <a href="#">ABOUT US</a>
    <a href="#">SERVICES</a>
    <a href="#">GALLERY</a>
    <a href="#">CONTACT US</a>
  </nav>
</header>

<section class="hero">
  <div class="abs hero-circle"></div>
  <div class="abs hero-photo" role="img" aria-label="White brick covered patio with lanterns, wicker seating and steel-framed glass doors"></div>
  <p class="abs hero-kicker">WELCOME TO</p>
  <h1 class="abs hero-title">Best <span>Interior</span><br>Design For Your Family</h1>
  <a class="btn" style="left:141px;top:414px">CONTACT US TODAY</a>
</section>

<section class="about">
  <div class="abs block-band" style="left:0;top:786px;width:565px;height:229px"></div>
  <div class="abs" role="img" aria-label="Bright living room with white sofas, fireplace and tall steel windows" style="left:0;top:850px;width:507px;height:461px;background:linear-gradient(160deg,#ecebea 0%,#d6d5d3 55%,#85817c 100%)"></div>
  <h2 class="abs section-title" style="left:609px;top:922px">ABOUT CLARA BETH HOLLOWAY</h2>
  <div class="abs rule" style="left:609px;top:976px"></div>
  <p class="abs about-text">Clara Beth Holloway has extensive experience in all aspects of interior design. She has worked on a wide array of residential and commercial projects in her hometown of Houston and across the United States. Clara Beth’s taste can best be described as a sophisticated blend of modern and contemporary styles that combine to create a clean, timeless space.</p>
  <a class="btn" style="left:610px;top:1186px">READ MORE</a>
</section>

<section class="services">
  <div class="abs block-band" style="left:635px;top:1395px;width:565px;height:229px"></div>
  <div class="abs" role="img" aria-label="White marble kitchen with stainless range hood and grey cabinetry" style="left:693px;top:1459px;width:507px;height:461px;background:linear-gradient(170deg,#f0efee 0%,#d8d8d8 50%,#9ea0a1 80%,#4f4b48 100%)"></div>
  <h2 class="abs section-title" style="left:141px;top:1508px">OUR SERVICES</h2>
  <div class="abs rule" style="left:141px;top:1562px"></div>
  <ul class="abs service-list">
    <li>Concept Origination and Project Management</li>
    <li>Review of Proposed Plans for New Construction and Remodels</li>
    <li>Procurement of Furniture, Accents, Art, Fixtures and Fittings</li>
    <li>Selection of Paints, Finishes and Construction Materials</li>
    <li>Vendor Coordination and Recommendations</li>
    <li>Home Staging, Styling and Editing</li>
  </ul>
  <a class="btn" style="left:141px;top:1817px">READ MORE</a>
</section>

<section class="gallery">
  <div class="abs gallery-band"></div>
  <h2 class="abs gallery-title">OUR GALLERY</h2>
  <div class="abs gallery-rule"></div>
  <div class="abs tile" style="left:141px"><div role="img" aria-label="White spiral staircase entry hall" style="background:linear-gradient(180deg,#f2f2f2 0%,#dcdcdb 70%,#5e5753 100%)"></div></div>
  <div class="abs tile" style="left:373px"><div role="img" aria-label="Modern dining room with white chairs" style="background:linear-gradient(180deg,#cdcccb 0%,#eeeeee 55%,#524d4a 100%)"></div></div>
  <div class="abs tile" style="left:606px"><div role="img" aria-label="Curved cream sofa with round coffee table" style="background:linear-gradient(180deg,#d8d8d7 0%,#eeeeed 60%,#cbcac8 100%)"></div></div>
  <div class="abs tile" style="left:838px"><div role="img" aria-label="Grey library sitting room with bookshelves and fireplace" style="background:linear-gradient(180deg,#6f7274 0%,#909395 50%,#c8c8c7 100%)"></div></div>
  <div class="abs swatch" style="left:22px;background:var(--accent)"></div>
  <div class="abs swatch" style="left:57px;background:var(--band)"></div>
  <a class="btn" style="left:539px;top:2457px">VIEW ALL</a>
</section>

<footer>
  <h3 class="abs foot-head" style="left:142px">QUICK LINKS</h3>
  <ul class="abs foot-links">
    <li>Home</li><li>About Us</li><li>Services</li><li>Gallery</li><li>Contact Us</li>
  </ul>

  <h3 class="abs foot-head" style="left:363px">CONTACT DETAILS</h3>
  <div class="abs contact-item" style="left:363px;top:2612px">
    <svg width="11" height="15" viewBox="0 0 11 15"><path d="M5.5 0A5.5 5.5 0 0 0 0 5.5C0 9.6 5.5 15 5.5 15S11 9.6 11 5.5A5.5 5.5 0 0 0 5.5 0zm0 7.6a2.1 2.1 0 1 1 0-4.2 2.1 2.1 0 0 1 0 4.2z" fill="#8a8a8a"/></svg>
    <div style="line-height:17px"><div style="font-size:11.5px;font-weight:500">CLARA BETH HOLLOWAY</div>123 Lorem ipsum dolor<br>sit amet</div>
  </div>
  <div class="abs contact-item" style="left:363px;top:2675px">
    <svg width="13" height="13" viewBox="0 0 13 13"><path d="M2.6 0.5l2 2.4-1.2 1.6c.8 1.8 2.3 3.3 4.1 4.1l1.6-1.2 2.4 2-1 2.1C5 11.8 1.2 8 .5 1.5z" fill="#8a8a8a"/></svg>
    <span>123-456-7890</span>
  </div>
  <div class="abs contact-item" style="left:363px;top:2706px">
    <svg width="13" height="10" viewBox="0 0 13 10" style="margin-top:3px"><rect width="13" height="10" fill="#8a8a8a"/><path d="M0 0l6.5 5.5L13 0" stroke="#fff" fill="none"/></svg>
    <span>info@clarabethholloway.example</span>
  </div>

  <h3 class="abs foot-head" style="left:683px">FOLLOW US</h3>
  <div class="abs social" style="left:683px;top:2617px"><i></i>Friendpage</div>
  <div class="abs social" style="left:683px;top:2654px"><i></i>Chirpline</div>
  <div class="abs social" style="left:683px;top:2692px"><i></i>Snapframe</div>

  <div class="abs foot-mark">CLARA BETH<br>HOLLOWAY</div>

  <div class="abs bottom-bar">Copyright © 2020 CLARA BETH HOLLOWAY. All Rights Reserved.</div>
</footer>

</body>
</html>
```